Business card for Les Brisants-Marins campsite

HORIZONTAL / 85x55
OBJECTIVE
Create a modern, attractive and memorable business card for the Les Brisants-Marins campsite, located on the Île d'Oléron.
The map should make people want to discover the campsite and immediately convey its world: ocean, holidays, nature and conviviality.
VISUAL IDENTITY
The design must be in the same graphic style as our website:
www.lesbrisants-marins.fr
The site is the main reference for the visual atmosphere: colours, typography, shapes, photographs and general universe.
The map and the site must give the impression of belonging to a single brand identity.
A UNIVERSE TO TRANSMIT
• Île d'Oléron
• Atlantic Ocean
• Seaside
• Direct access to the beaches
• Vacation
• Nature
• Family-friendly and welcoming atmosphere
• Relaxation
DESIRED STYLE
Bright, warm, modern, nautical and natural.
We want a creation with a real personality, immediately recognizable, and not a generic camping business card.
FRONT
Prioritize visual impact with:
• Official logo Les Brisants-Marins
• Île d'Oléron
• A strong evocation of the ocean and holidays
• A short and memorable hook
The designer is free to propose their own hook.
BACK
The Marine Breakers
Villages 1 & 2
22 Rue des Vergnes
17310 Saint-Pierre-d'Oléron
France
Tel.: +33 5 46 82 13 47
www.lesbrisants-marins. fr
Possibility of discreet integration:
Direct access to the beaches
Mobile homes • Pitches • Accommodation
Le Varech Bar-Restaurant
FORMAT
Double-sided card: 85 × 55 mm.
Horizontal orientation
AVOID
• Overly institutional design
• Overloaded map
• Generic "camping" style
• Too many pictograms
• Accumulation of texts
• Modification or distortion of the official logo
• Graphic design unrelated to the website
CREATIVE FREEDOM
We are looking for an original proposal.
The designer can play with the graphic codes of the ocean, waves, sun, beach and Île d'Oléron, while remaining faithful to the visual identity of the site.
The card must be aesthetically pleasing and original enough to make people want to keep it.
The objective:
See the map → think about the ocean and holidays → remember Les Brisants-Marins → discover the campsite.
Target Market(s)
All targets
Industry/Entity Type
Tourisme
Contact Information for Business Card
adresse, téléphone, email, site internet + réseaux sociaux
Look and feel
Each slider illustrates characteristics of the customer's brand and the style your logo design should communicate.

```html
<!DOCTYPE html>
<html lang="fr">
<head>
<meta charset="utf-8">
<title>Les Brisants-Marins – carte de visite</title>
<link rel="stylesheet" href="https://fonts.googleapis.com/css2?family=Spectral:wght@400;500&family=Parisienne&display=swap">
<style>
  :root{
    --board:#e3e3e3;
    --card:#ffffff;
    --ocean:#0b78bb;
    --lime:#9bc13b;
    --ink:#222222;
    --grey:#4a4a4a;
    --sea-deep:#1d5f8c;
    --sea-light:#6fb3d6;
    --sand:#c9a476;
    --serif:'Spectral', Georgia, serif;
    --script:'Parisienne', cursive;
  }
  *{box-sizing:border-box;margin:0;padding:0}
  html,body{width:1200px;height:1107px;overflow:hidden;background:var(--board)}
  .board{position:relative;width:1200px;height:1107px}
  .side-label{position:absolute;font-family:var(--serif);font-weight:400;font-size:66px;color:var(--ocean);letter-spacing:2px}
  .side-label.front{left:100px;top:250px}
  .side-label.back{left:113px;top:760px}
  .card{position:absolute;left:370px;width:788px;height:510px;background:var(--card);overflow:hidden}
  .card.front{top:42px}
  .card.back{top:573px}

  .brand{position:absolute;display:flex;align-items:center;gap:12px;font-family:var(--serif);font-weight:500;color:var(--grey)}
  .brand-dot{width:34px;height:34px;border-radius:50%;background:var(--ocean);flex:none}
  .front .brand{left:40px;top:104px;font-size:29px}
  .back .brand{left:58px;top:168px;font-size:25px}

  .photo{position:absolute;left:340px;top:0;width:448px;height:510px;
    background:linear-gradient(180deg,#cfe3f0 0%,#9cc6e0 12%,var(--sea-deep) 30%,var(--sea-light) 55%,var(--sand) 72%,#8c7a55 100%)}
  .photo::after{content:"";position:absolute;inset:0;background:linear-gradient(90deg,#fff 0%,rgba(255,255,255,.6) 12%,rgba(255,255,255,0) 30%)}
  .island-tag{position:absolute;left:377px;top:156px;width:236px;height:38px;background:var(--lime);border-radius:4px;
    font-family:var(--serif);font-size:20px;color:#fff;text-align:center;line-height:38px;letter-spacing:1px}
  .hook{position:absolute;font-family:var(--script);font-size:46px;line-height:1}
  .hook.l1{left:30px;top:226px;color:var(--ink)}
  .hook.l2{left:86px;top:282px;color:var(--ocean)}
  .hook-line{position:absolute;left:165px;top:332px}

  .waves{position:absolute;left:0;top:0}

  .contacts{position:absolute;left:423px;top:70px;list-style:none;font-family:var(--serif);font-size:17px;color:var(--ink);letter-spacing:.4px}
  .contacts li{position:relative;padding-left:42px;line-height:23px}
  .contacts svg{position:absolute;left:0;top:2px}
  .contacts .addr{height:99px}
  .contacts .tel{height:53px}
  .contacts .web{height:54px}
  .divider{position:absolute;left:115px;top:335px;width:555px;height:1px;background:linear-gradient(90deg,rgba(0,0,0,0),#bbb 20%,#bbb 80%,rgba(0,0,0,0))}
  .feature{position:absolute;top:368px;display:flex;gap:10px;font-family:var(--serif)}
  .feature .badge{width:41px;height:41px;border-radius:50%;background:var(--lime);flex:none;display:flex;align-items:center;justify-content:center}
  .feature h3{font-weight:500;font-size:15.5px;color:var(--ocean);letter-spacing:.8px;line-height:18px}
  .feature p{font-size:12px;color:var(--ink);letter-spacing:.8px;line-height:17px}
  .f1{left:90px}.f2{left:310px}.f3{left:534px}
</style>
</head>
<body>
<div class="board">
  <div class="side-label front">Front</div>
  <div class="side-label back">Back</div>

  <section class="card front">
    <div class="photo" role="img" aria-label="Vue aérienne de la plage, de l'océan et du camping avec une carte de l'Île d'Oléron"></div>
    <div class="brand"><span class="brand-dot"></span>Les Brisants-Marins</div>
    <div class="island-tag">ÎLE D'OLÉRON</div>
    <div class="hook l1">Votre parenthèse</div>
    <div class="hook l2">face à l'océan</div>
    <svg class="hook-line" width="200" height="20" viewBox="0 0 200 20">
      <path d="M2 8 C60 4 140 4 198 6" stroke="#0b78bb" stroke-width="2" fill="none"/>
      <path d="M10 14 C70 10 130 10 180 11" stroke="#0b78bb" stroke-width="1.5" fill="none"/>
    </svg>
    <svg class="waves" width="788" height="510" viewBox="0 0 788 510">
      <path d="M0 436 C110 472 250 452 400 430 C470 420 530 426 575 452 L650 510 L0 510 Z" fill="#fff"/>
      <path d="M455 425 C540 420 600 450 650 485 L680 510 L640 510 C600 470 540 436 455 425 Z" fill="#9bc13b"/>
      <path d="M0 441 C120 476 270 460 410 434 C480 424 530 432 570 462 L615 510 L0 510 Z" fill="#0b78bb"/>
    </svg>
  </section>

  <section class="card back">
    <div class="brand"><span class="brand-dot"></span>Les Brisants-Marins</div>
    <ul class="contacts">
      <li class="addr">
        <svg width="20" height="26" viewBox="0 0 20 26"><path d="M10 0C4.5 0 1 4 1 9c0 6 9 15 9 15s9-9 9-15c0-5-3.5-9-9-9z" fill="#0b78bb"/><circle cx="10" cy="9" r="3.5" fill="#fff"/><rect x="4" y="24" width="12" height="2" fill="#0b78bb"/></svg>
        The Marine Breakers Villages 1 &amp; 2<br>22 Rue des Vergnes 17310<br>Saint-Pierre-d'Oléron France
      </li>
      <li class="tel">
        <svg width="20" height="20" viewBox="0 0 20 20"><path d="M4 1l4 4-2 3c1 3 3 5 6 6l3-2 4 4-3 3C9 19 1 11 1 4z" fill="#0b78bb"/></svg>
        +33 5 46 82 13 47
      </li>
      <li class="web">
        <svg width="22" height="22" viewBox="0 0 22 22"><circle cx="11" cy="11" r="10" fill="#0b78bb"/><g stroke="#fff" stroke-width="1.3" fill="none"><ellipse cx="11" cy="11" rx="4" ry="10"/><path d="M1 11h20M3 6h16M3 16h16"/></g></svg>
        www.lesbrisants-marins.fr
      </li>
      <li>
        <svg width="24" height="18" viewBox="0 0 24 18"><rect width="24" height="18" rx="2" fill="#0b78bb"/><path d="M1 2l11 8 11-8" stroke="#fff" stroke-width="1.6" fill="none"/></svg>
        contact@lesbrisants-marins.fr
      </li>
    </ul>
    <div class="divider"></div>

    <div class="feature f1">
      <span class="badge"><svg width="22" height="22" viewBox="0 0 22 22"><circle cx="15" cy="6" r="4" fill="#fff"/><path d="M2 18c6-3 12-3 18 0v2H2z" fill="#fff"/></svg></span>
      <div><h3>ACCÈS DIRECT</h3><p>AUX PLAGES</p></div>
    </div>
    <div class="feature f2">
      <span class="badge"><svg width="22" height="22" viewBox="0 0 22 22"><path d="M2 10l9-7 9 7v9H2z" fill="#fff"/><rect x="9" y="13" width="4" height="6" fill="#9bc13b"/></svg></span>
      <div><h3>MOBIL-HOMES</h3><p>•EMPLACEMENTS<br>•HEBERGEMENTS</p></div>
    </div>
    <div class="feature f3">
      <span class="badge"><svg width="22" height="22" viewBox="0 0 22 22"><path d="M5 3h12l-2 9H7z" fill="#fff"/><rect x="10" y="12" width="2" height="6" fill="#fff"/><rect x="6" y="18" width="10" height="2" fill="#fff"/></svg></span>
      <div><h3>LE VARECH</h3><p>BAR-RESTAURANT</p></div>
    </div>

    <svg class="waves" width="788" height="510" viewBox="0 0 788 510">
      <path d="M420 440 C500 436 560 456 610 480 L650 510 L630 510 C590 480 520 448 420 440 Z" fill="#9bc13b"/>
      <path d="M0 451 C90 480 200 476 320 452 C400 436 460 434 520 448 C560 460 590 482 620 510 L0 510 Z" fill="#0b78bb"/>
    </svg>
  </section>
</div>
</body>
</html>
```